KAZ Freightworks #ALLKAZ Business Cards & Letterhead

I am looking to business cards designed for our organization. We are currently undergoing a small re-branding that is taking place. Our organization is called KAZ Freightworks and we are headquartered in Phoenix, AZ. We primarily provide transportation and logistics services to the Meridel Parcel Bureau who is our largest customer. I would like to see a design that incorporates name, title, contact info, website, and address (this will be different depending on the employee). I would also like to see some color on the business card using our logo colors or a variation. I would like our logo on the back of the business card with the website displayed. The final design should communicate that we are a next generation transportation operate that focuses on being driver-first, customer-centric, innovative, and sustainable.We would also like our #ALLKAZ catch phrase incorporated as well.
Updates

Decision maker traveling outside of the country until Monday, November 25th.

Target Market(s)

Transportation & Logistics

Industry/Entity Type

Trucking Company

Contact Information for Business Card

-First and Last Name
-Position Title
-Contact Phone
-Contact Email
-Physical Address

Font styles to use
Serif

Colors

Designer to choose colors to be used in the design.

Requirements
Must have
• -KAZ logo prominently displayed
• -#ALLKAZ catch phrase used
• -Some amount of color, design gradient, etc.
• -Logo on the back with website listed (https://www.kazfreightco.example)

```html
<!DOCTYPE html>
<html lang="en">
<head>
<meta charset="utf-8">
<title>KAZ Freightworks Business Card</title>
<link href="https://fonts.googleapis.com/css2?family=Roboto+Slab:wght@400;700;900&display=swap" rel="stylesheet">
<style>
  :root {
    --backdrop: #3a3a3a;
    --card-black: #1b1c1d;
    --teal: #073f4c;
    --lime: #7cc52a;
    --white: #ffffff;
    --silver: #8e9091;
  }
  * { margin: 0; padding: 0; box-sizing: border-box; }
  html, body { width: 799px; height: 1200px; overflow: hidden; }
  body {
    background: var(--backdrop);
    font-family: "Roboto Slab", Georgia, serif;
    position: relative;
  }
  .card {
    position: absolute;
    left: 90px;
    width: 620px;
    height: 354px;
    overflow: hidden;
    background: var(--card-black);
    box-shadow: 0 10px 24px rgba(0,0,0,0.45);
  }
  .card-front { top: 150px; }
  .card-back  { top: 700px; }

  /* Front */
  .front-brand {
    position: absolute;
    left: 0; right: 0; top: 100px;
    display: flex; align-items: center; justify-content: center; gap: 14px;
  }
  .front-dot { width: 18px; height: 18px; border-radius: 50%; background: var(--silver); }
  .front-name {
    font-weight: 900;
    font-size: 62px;
    line-height: 1;
    color: var(--silver);
    letter-spacing: 2px;
  }
  .front-web {
    position: absolute;
    left: 0; right: 0; top: 252px;
    display: flex; align-items: center; justify-content: center; gap: 18px;
    color: var(--white);
    font-size: 14px;
    letter-spacing: 3px;
  }
  .front-web .dash { width: 36px; height: 3px; background: var(--lime); }

  /* Back */
  .back-art { position: absolute; inset: 0; }
  .back-brand {
    position: absolute;
    left: 40px; top: 130px;
    width: 210px;
    display: flex; align-items: center; justify-content: center; gap: 12px;
  }
  .back-dot { width: 20px; height: 20px; border-radius: 50%; background: var(--lime); flex: none; }
  .back-name {
    font-weight: 900;
    font-size: 72px;
    line-height: 1;
    color: var(--white);
    letter-spacing: 1px;
  }
  .info {
    position: absolute;
    left: 318px; top: 56px;
    color: var(--white);
  }
  .person-name { font-weight: 700; font-size: 25px; line-height: 1.15; }
  .person-title {
    font-size: 15px;
    padding-bottom: 5px;
    border-bottom: 2px solid var(--lime);
    display: inline-block;
    padding-right: 60px;
    margin-bottom: 10px;
  }
  .contact-list { list-style: none; }
  .contact-list li {
    display: flex; align-items: center; gap: 10px;
    font-size: 14.5px; line-height: 22px;
  }
  .contact-list svg { width: 14px; height: 14px; flex: none; }
  .company-name { color: var(--lime); font-weight: 700; font-size: 15px; margin-top: 4px; }
  .address { font-size: 14.5px; line-height: 20px; }
  .catchphrase { color: var(--lime); font-weight: 700; font-size: 15px; margin-top: 10px; letter-spacing: 1px; }
</style>
</head>
<body>

<section class="card card-front" aria-label="Business card front">
  <div class="front-brand"><span class="front-dot"></span><span class="front-name">KAZ</span></div>
  <div class="front-web"><span class="dash"></span><span>www.kazfreightco.example</span><span class="dash"></span></div>
</section>

<section class="card card-back" aria-label="Business card back">
  <svg class="back-art" viewBox="0 0 620 354" width="620" height="354" aria-hidden="true">
    <path d="M300 0 Q 250 230 135 354 L620 354 L620 0 Z" fill="var(--teal)"/>
    <path d="M296 0 Q 246 230 128 354" fill="none" stroke="var(--lime)" stroke-width="7"/>
  </svg>

  <div class="back-brand"><span class="back-dot"></span><span class="back-name">KAZ</span></div>

  <div class="info">
    <div class="person-name">Calder Voss</div>
    <div class="person-title">Chairman &amp; CEO</div>
    <ul class="contact-list">
      <li>
        <svg viewBox="0 0 16 16"><path d="M3 1h3l1.5 4-2 1.2a9 9 0 0 0 4.3 4.3L11 8.5l4 1.5v3a2 2 0 0 1-2 2C6.5 15 1 9.5 1 3a2 2 0 0 1 2-2z" fill="var(--lime)"/></svg>
        555-014-2290
      </li>
      <li>
        <svg viewBox="0 0 16 16"><rect x="1" y="3" width="14" height="10" fill="var(--lime)"/><path d="M1 3l7 6 7-6" fill="none" stroke="var(--teal)" stroke-width="1.5"/></svg>
        calder@kazfreightco.example
      </li>
      <li>
        <svg viewBox="0 0 16 16"><circle cx="8" cy="8" r="6.5" fill="none" stroke="var(--lime)" stroke-width="1.6"/><ellipse cx="8" cy="8" rx="2.8" ry="6.5" fill="none" stroke="var(--lime)" stroke-width="1.4"/><path d="M1.5 8h13" stroke="var(--lime)" stroke-width="1.4"/></svg>
        www.kazfreightco.example
      </li>
    </ul>
    <div class="company-name">KAZ Freightworks &amp; Energy</div>
    <div class="address">4170 North Saguaro Ridge<br>Drive Glendale, AZ 85000</div>
    <div class="catchphrase">#ALLKAZ</div>
  </div>
</section>

</body>
</html>
```